Hydraulics Company Business Card Design

Modern business card design for a hydraulics company.
Our company colours are - black, orange and white.
I would like the following contact details included-
Name
Position
Phone number
Email
Website
Street Address

I have attached our company logo.
I would like the back of the card white.

Thank you.

```html
<!DOCTYPE html>
<html lang="en">
<head>
<meta charset="utf-8">
<title>Riverbend Hydraulics – Business Card</title>
<link href="https://fonts.googleapis.com/css2?family=Montserrat:wght@400;500;700;800&display=swap" rel="stylesheet">
<style>
  :root {
    --orange: #f89c1c;
    --black: #1f1f1f;
    --white: #ffffff;
    --stage: #2c2c2c;
    --ink: #2a2a2a;
  }
  * { margin: 0; padding: 0; box-sizing: border-box; }
  html, body { width: 1200px; height: 875px; overflow: hidden; }
  body {
    background: var(--stage);
    font-family: "Montserrat", sans-serif;
    display: flex;
    align-items: center;
    justify-content: center;
    gap: 40px;
  }
  .card {
    position: relative;
    width: 540px;
    height: 310px;
    border-radius: 22px;
    background: var(--white);
    overflow: hidden;
    box-shadow: 0 20px 40px rgba(0,0,0,0.45);
  }

  /* Logo side */
  .card--front .band {
    position: absolute;
    left: 0; right: 0;
    top: 196px;
    height: 8px;
    background: var(--orange);
  }
  .card--front .wordmark {
    position: absolute;
    left: 0; right: 0;
    top: 92px;
    text-align: center;
    color: var(--orange);
    font-weight: 800;
    font-size: 44px;
    line-height: 1.05;
    letter-spacing: -0.5px;
  }
  .wordmark .line { display: block; }

  /* Contact side */
  .card--back .frame { position: absolute; inset: 0; }
  .card--back .panel-wordmark {
    position: absolute;
    left: 0; width: 240px;
    top: 124px;
    text-align: center;
    color: var(--orange);
    font-weight: 800;
    font-size: 24px;
    line-height: 1.1;
  }
  .contact {
    position: absolute;
    left: 278px;
    top: 46px;
    color: var(--ink);
  }
  .contact__name {
    color: var(--orange);
    font-weight: 800;
    font-size: 25px;
    letter-spacing: 0.5px;
  }
  .contact__role {
    font-size: 13px;
    font-weight: 500;
    margin-top: 2px;
    margin-bottom: 22px;
  }
  .contact__list { list-style: none; }
  .contact__item {
    display: flex;
    align-items: flex-start;
    gap: 10px;
    font-size: 12px;
    line-height: 1.45;
    margin-bottom: 6px;
  }
  .contact__item svg { flex: none; width: 12px; height: 12px; margin-top: 3px; }
</style>
</head>
<body>

  <section class="card card--front" aria-label="Card front">
    <div class="wordmark">
      <span class="line">Riverbend</span>
      <span class="line">Hydraulics</span>
    </div>
    <div class="band"></div>
  </section>

  <section class="card card--back" aria-label="Card back">
    <svg class="frame" width="540" height="310" viewBox="0 0 540 310" aria-hidden="true">
      <path d="M0 0 H214 Q254 0 254 40 V262 Q254 294 286 294 H540 V310 H0 Z" fill="#f89c1c"/>
      <path d="M0 12 H204 Q240 12 240 48 V252 Q240 284 206 284 H0 Z" fill="#1f1f1f"/>
    </svg>
    <div class="panel-wordmark">Riverbend<br>Hydraulics</div>

    <div class="contact">
      <div class="contact__name">MARCUS HALE</div>
      <div class="contact__role">Founder &amp; CEO</div>
      <ul class="contact__list">
        <li class="contact__item">
          <svg viewBox="0 0 12 12"><path d="M6 0.5a4 4 0 0 0-4 4c0 3 4 7 4 7s4-4 4-7a4 4 0 0 0-4-4zm0 5.5a1.5 1.5 0 1 1 0-3 1.5 1.5 0 0 1 0 3z" fill="#f89c1c"/></svg>
          <span>Street Address Here, City<br>State, Country, ZIP 123</span>
        </li>
        <li class="contact__item">
          <svg viewBox="0 0 12 12"><path d="M2.5 1l2 2.2-1 1.3a7 7 0 0 0 4 4l1.3-1 2.2 2-1.3 1.5C5 10.8 1.2 7 .9 2.3z" fill="#f89c1c"/></svg>
          <span>(123) 456-7890</span>
        </li>
        <li class="contact__item">
          <svg viewBox="0 0 12 12"><rect x="0.5" y="2" width="11" height="8" rx="1" fill="#f89c1c"/><path d="M1 2.5l5 4 5-4" stroke="#fff" stroke-width="1" fill="none"/></svg>
          <span>info@yourwebsitehere.com</span>
        </li>
        <li class="contact__item">
          <svg viewBox="0 0 12 12"><circle cx="6" cy="6" r="5" fill="none" stroke="#f89c1c" stroke-width="1.4"/><path d="M1 6h10M6 1c-2.5 3-2.5 7 0 10M6 1c2.5 3 2.5 7 0 10" stroke="#f89c1c" stroke-width="1" fill="none"/></svg>
          <span>yourwebsitehere.com</span>
        </li>
      </ul>
    </div>
  </section>

</body>
</html>
```